Need flyer for honey

I need the advertising flyer for my honey products. Will need around 4-6 page A5 size. Flyer content is ready but will need to check the wording and need the artwork and pictures designed in a proper manner.

Advertising

```html
<!DOCTYPE html>
<html lang="en">
<head>
<meta charset="utf-8">
<title>Amber Hollow – Honey Brochure</title>
<link rel="stylesheet" href="https://fonts.googleapis.com/css2?family=Cinzel:wght@700&family=Tinos:wght@400&display=swap">
<style>
  :root {
    --backdrop: #5a5a5a;
    --page-light: #ffffff;
    --page-shade: #e6e6e6;
    --ink: #1b1b1b;
    --muted: #555555;
    --gold: #d99a12;
    --honey: #f4b21b;
    --honey-deep: #eea20c;
    --brown: #7a3d1c;
    --brown-dark: #5c2a12;
    --cream: #fde6c4;
    --banner: #f0a81a;
  }
  * { box-sizing: border-box; margin: 0; padding: 0; }
  html, body { width: 1200px; height: 907px; overflow: hidden; }
  body { background: var(--backdrop); position: relative; font-family: "Tinos", "Times New Roman", serif; color: var(--ink); }

  .brochure {
    position: absolute; left: 65px; top: 70px; width: 1072px; height: 763px;
    overflow: hidden; box-shadow: 0 6px 18px rgba(0,0,0,.45);
  }
  .page { position: absolute; top: 0; height: 100%; }
  .page--left { left: 0; width: 540px; background: linear-gradient(180deg, var(--page-light) 0%, #f2f2f2 60%); }
  .page--right { left: 540px; width: 532px; background: linear-gradient(90deg, var(--page-shade) 0%, #f6f6f6 35%, var(--page-light) 100%); }

  .artwork { position: absolute; inset: 0; width: 100%; height: 100%; }

  .badge {
    position: absolute; left: 0; top: 42px; width: 307px; height: 40px;
    background: var(--banner); border-radius: 0 20px 20px 0;
    box-shadow: 0 3px 4px rgba(0,0,0,.25);
    font-family: "Cinzel", "Times New Roman", serif; font-weight: 700;
    font-size: 22px; line-height: 42px; padding-left: 33px; color: var(--ink);
  }
  .intro {
    position: absolute; left: 32px; top: 111px; width: 487px;
    font-size: 14.4px; line-height: 18.2px; text-align: justify;
  }
  .contact-title {
    position: absolute; left: 34px; top: 284px;
    font-family: "Cinzel", "Times New Roman", serif; font-weight: 700; font-size: 25px; letter-spacing: .5px;
  }
  .contact-list { position: absolute; top: 329px; list-style: none; font-size: 14.4px; line-height: 18.2px; }
  .contact-list--address { left: 30px; }
  .contact-list--lines { left: 196px; top: 326px; }
  .contact-list li { display: flex; gap: 6px; align-items: flex-start; }
  .contact-list svg { width: 9px; height: 9px; margin-top: 4px; flex: none; fill: var(--muted); }
  .indent { padding-left: 15px; }

  .brand-name {
    position: absolute; left: 540px; width: 532px; top: 52px; text-align: center;
    font-family: "Cinzel", "Times New Roman", serif; font-weight: 700;
    font-size: 50px; line-height: 1; color: var(--gold);
  }
  .tagline {
    position: absolute; left: 540px; width: 532px; top: 130px; text-align: center;
    font-family: "Tinos", "Times New Roman", serif; font-size: 21px; color: var(--ink);
  }
</style>
</head>
<body>
  <main class="brochure">
    <section class="page page--left"></section>
    <section class="page page--right"></section>

    <svg class="artwork" viewBox="0 0 1072 763" preserveAspectRatio="none">
      <defs>
        <linearGradient id="brownBand" x1="0" y1="0" x2="1" y2="0">
          <stop offset="0" stop-color="var(--brown-dark)"/>
          <stop offset=".5" stop-color="var(--brown)"/>
          <stop offset="1" stop-color="#a65a1e"/>
        </linearGradient>
        <linearGradient id="honeyBase" x1="0" y1="0" x2="0" y2="1">
          <stop offset="0" stop-color="var(--honey-deep)"/>
          <stop offset="1" stop-color="var(--honey)"/>
        </linearGradient>
        <radialGradient id="jarTone" cx=".4" cy=".55" r=".6">
          <stop offset="0" stop-color="#f7a63a"/>
          <stop offset=".75" stop-color="#e08a1a"/>
          <stop offset="1" stop-color="#b8681c"/>
        </radialGradient>
      </defs>

      <path class="wave wave--orange" d="M700,400 C850,360 960,320 1072,280 L1072,440 C950,470 820,470 700,450 Z" fill="var(--honey-deep)"/>
      <path class="wave wave--cream" d="M700,450 C820,470 950,450 1072,420 L1072,445 C950,478 820,485 700,465 Z" fill="var(--cream)"/>
      <path class="wave wave--honey" d="M0,560 C200,470 400,450 600,490 C800,530 950,520 1072,470 L1072,763 L0,763 Z" fill="url(#honeyBase)" role="img" aria-label="Honeycomb pattern in golden yellow"/>
      <path class="wave wave--brown" d="M0,520 C200,420 420,400 620,440 C800,475 950,470 1072,445 L1072,475 C950,520 800,530 600,490 C400,450 200,470 0,560 Z" fill="url(#brownBand)"/>

      <rect class="photo photo--jar" x="620" y="175" width="345" height="395" rx="40" fill="url(#jarTone)" role="img" aria-label="Photo of a glass jar of honey with a wooden dipper spoon and pieces of honeycomb"/>
      <ellipse class="photo photo--bee" cx="165" cy="632" rx="80" ry="45" fill="#c98a2a" opacity=".8" role="img" aria-label="Photo of a honey bee in flight"/>
    </svg>

    <div class="badge">HACCP Certified</div>
    <p class="intro">Amber Hollow’s Factory is HACCP certified. HACCP (Hazard Analysis and Critical Control Points) which is most popular around the world food industry is a risk management system that identifies, evaluates, and controls hazards related to food safety throughout the food supply chain. Amber Hollow has a detailed QA system and incorporates this into our daily work environment to make sure every batch of our honey is with the uniform safety standard.</p>

    <h2 class="contact-title">Contact Us</h2>
    <ul class="contact-list contact-list--address">
      <li><svg viewBox="0 0 10 10"><path d="M5 0a3.5 3.5 0 0 0-3.5 3.5C1.5 6 5 10 5 10s3.5-4 3.5-6.5A3.5 3.5 0 0 0 5 0zm0 5a1.5 1.5 0 1 1 0-3 1.5 1.5 0 0 1 0 3z"/></svg>Name Surname</li>
      <li class="indent">House no., Street,</li>
      <li class="indent">Place, State</li>
    </ul>
    <ul class="contact-list contact-list--lines">
      <li><svg viewBox="0 0 10 10"><path d="M2 0 4 2.5 3 3.8c.7 1.4 1.8 2.5 3.2 3.2L7.5 6 10 8l-1.3 1.6C4.5 9.6.4 5.5.4 1.3z"/></svg>123-456-789</li>
      <li><svg viewBox="0 0 10 10"><path d="M0 2h10v6H0z"/></svg>Dummy@email.com</li>
      <li><svg viewBox="0 0 10 10"><circle cx="5" cy="5" r="4"/></svg>www.website.com</li>
    </ul>

    <h1 class="brand-name">Amber Hollow</h1>
    <p class="tagline">Pure Honey, Gathered With Care</p>
  </main>
</body>
</html>
```